Presentation website to our app

We have a really nice postcard app named Snapforpost.com, however we do not have any website that presents the app and what you can do with it.
If you go to www.snapforpost.com you just get the app directly.
I would like to change this, so that we get a "real" website on www.snapforpost.com, where we can present "What is this?". Then there should be a button to click on, in order to create an account or to login to the app.
The design should be responsive, so that the design should look good on both PC and Smartphone.
Please don't think in keeping the design as it is now on www.snapforpost.com - you should re-think it.
Design needs to be really simple, innovative and needs to show what Snapforpost.com can be used for.
I like these designs:
https://www.pavlora.com/
https://dayvorix.com/hello
Updates
Hi,
Just to let you all know - I have not added any designs that I like, but this one is really cool:
Regards,
Hi,
I also like: https://www.pavlora.com/
Regards

```html
<!DOCTYPE html>
<html lang="en">
<head>
<meta charset="utf-8">
<title>Snap for Post – Online postcard app</title>
<link href="https://fonts.googleapis.com/css2?family=PT+Sans:wght@400;700&display=swap" rel="stylesheet">
<style>
:root{
  --teal:#3d9cc6;
  --teal-dark:#2f86ad;
  --footer:#55a6cb;
  --ink:#3a3a3a;
  --muted:#6b6b6b;
  --rule:#dcdcdc;
  --band:#ececec;
  --white:#fff;
}
*{box-sizing:border-box;margin:0;padding:0}
html,body{width:746px;height:1200px;overflow:hidden;background:var(--white)}
body{font-family:"PT Sans",Arial,sans-serif;color:var(--ink);position:relative}
a{color:inherit;text-decoration:none}
.abs{position:absolute}
/* header */
.site-header{position:absolute;left:0;top:0;width:746px;height:49px;background:var(--white)}
.brand{position:absolute;left:113px;top:8px;display:flex;align-items:center;gap:4px}
.brand-mark{width:31px;height:31px;border-radius:6px;background:var(--teal)}
.brand-name{font-size:13px;line-height:12px;color:var(--teal);font-weight:700;width:40px}
.main-nav{position:absolute;top:21px;left:0;width:746px;font-size:7.5px}
.main-nav a{position:absolute;color:var(--ink);white-space:nowrap}
/* hero */
.hero{position:absolute;left:0;top:49px;width:746px;height:317px;
  background:linear-gradient(90deg,#6a5a4c 0%,#8b7562 30%,#a78f79 55%,#8d7765 80%,#6e6457 100%)}
.hero-arrow{position:absolute;top:136px;width:32px;height:32px;border-radius:50%;border:2px solid rgba(255,255,255,.45)}
.hero-title{position:absolute;left:0;width:746px;top:210px;text-align:center;color:var(--white);font-size:25px;font-weight:400}
.hero-sub{position:absolute;left:130px;width:486px;top:247px;text-align:center;color:var(--white);font-size:10px;line-height:16px}
/* sections */
.section-title{position:absolute;left:0;width:746px;text-align:center;color:var(--teal);font-size:15px;font-weight:400}
.section-lead{position:absolute;left:130px;width:486px;text-align:center;font-size:6.2px;line-height:12px;color:var(--muted)}
.rule{position:absolute;left:117px;width:509px;height:1px;background:var(--rule)}
.feature{position:absolute;top:484px;width:160px;text-align:center}
.feature svg{display:block;margin:0 auto;height:34px}
.feature h3{font-size:7.5px;font-weight:700;margin-top:9px;color:var(--ink)}
.feature p{font-size:5.4px;line-height:11.6px;color:var(--muted);margin-top:7px;padding:0 4px}
.service{position:absolute;top:703px;width:160px}
.service-photo{width:160px;height:80px}
.service h3{font-size:7.5px;font-weight:700;margin-top:11px;color:var(--ink)}
/* what is this */
.band{position:absolute;left:0;top:834px;width:746px;height:204px;background:var(--band)}
.laptop{position:absolute;left:113px;top:852px}
.band-title{position:absolute;left:411px;top:863px;color:var(--teal);font-size:15px;font-weight:400}
.band-text{position:absolute;left:412px;top:888px;width:222px;font-size:5.5px;line-height:10.6px;color:var(--muted)}
.band-button{position:absolute;left:412px;top:967px;width:132px;height:25px;background:var(--teal);border:1px solid var(--teal-dark);color:var(--white);font-size:7.5px;line-height:23px;text-align:center}
/* clients */
.clients-title{position:absolute;left:112px;top:1051px;color:var(--teal);font-size:14px;font-weight:400}
.clients-nav{position:absolute;left:619px;top:1061px;font-size:8px;color:#888;letter-spacing:4px}
.client{position:absolute;top:1081px;width:99px;height:56px;border:1px solid #e2e2e2;display:flex;align-items:center;justify-content:center;font-size:10px;font-weight:700;color:#444}
/* footer */
.site-footer{position:absolute;left:0;top:1157px;width:746px;height:43px;background:var(--footer);color:var(--white)}
.footer-links{position:absolute;left:113px;top:11px;font-size:5px;letter-spacing:.2px}
.footer-links span{margin:0 6px}
.copyright{position:absolute;left:113px;top:26px;font-size:5px}
.follow{position:absolute;left:509px;top:20px;font-size:5px}
.social{position:absolute;top:13px;width:16px;height:16px;border-radius:50%;background:#2f6f96}
</style>
</head>
<body>
<header class="site-header">
  <div class="brand"><div class="brand-mark"></div><div class="brand-name">snap for post</div></div>
  <nav class="main-nav">
    <a style="left:345px">Home</a>
    <a style="left:402px">About us</a>
    <a style="left:468px">Services</a>
    <a style="left:531px">Features</a>
    <a style="left:595px">Contact&nbsp; Us</a>
  </nav>
</header>

<section class="hero" role="img" aria-label="Two young women looking at a smartphone together outdoors">
  <div class="hero-arrow" style="left:43px"></div>
  <div class="hero-arrow" style="left:667px;opacity:.5"></div>
  <h1 class="hero-title">We are an online postcard app</h1>
  <p class="hero-sub">Turn the photos on your phone into real printed postcards in a few taps, and we post them anywhere in the world for you.</p>
</section>

<h2 class="section-title" style="top:386px">Welcome to Snap for Post</h2>
<p class="section-lead" style="top:415px">Snap for Post lets you pick a photo, write a personal message and send a real paper postcard straight from your computer or phone. We print it on thick card and post it the same day, so friends and family get something they can hold, keep and pin to the fridge.</p>
<div class="rule" style="top:460px"></div>

<div class="feature" style="left:108px">
  <svg viewBox="0 0 40 30" width="40"><rect x="5" y="2" width="30" height="20" fill="none" stroke="#666" stroke-width="2.5"/><rect x="1" y="24" width="38" height="4" fill="#666"/></svg>
  <h3>Create on any screen</h3>
  <p>Design your card on a laptop, tablet or phone. Choose a photo, add a short note and the address, and preview it exactly as it will arrive.</p>
</div>
<div class="feature" style="left:292px">
  <svg viewBox="0 0 34 30" width="34"><g fill="#666"><rect x="1" y="20" width="5" height="10"/><rect x="8" y="16" width="5" height="14"/><rect x="15" y="18" width="5" height="12"/><rect x="22" y="12" width="5" height="18"/><rect x="29" y="8" width="5" height="22"/></g><polyline points="3,14 10,9 17,11 24,5 31,2" fill="none" stroke="#666" stroke-width="1.5"/></svg>
  <h3>Track every card</h3>
  <p>See when each postcard is printed and posted. Send one card or a hundred, and keep all your sent cards and addresses in one place.</p>
</div>
<div class="feature" style="left:475px">
  <svg viewBox="0 0 34 34" width="34"><path d="M8 30 Q2 22 6 14 L12 4 Q14 2 16 4 L15 12 L22 2 Q25 1 25 4 L20 14 L28 6 Q31 6 30 9 L22 20 Q30 16 31 19 L20 30 Q14 34 8 30 Z" fill="#666"/></svg>
  <h3>Say hello by post</h3>
  <p>Holidays, birthdays, thank-yous or just because. A real card in the mailbox says more than a message that is gone in one scroll.</p>
</div>
<div class="rule" style="top:616px"></div>

<h2 class="section-title" style="top:635px">Our Services</h2>
<p class="section-lead" style="top:661px">Use Snap for Post for yourself or for your business. Send greetings to family, thank customers after an order or invite guests to your event. Every card is printed in full colour on premium stock and delivered by regular post.</p>

<div class="service" style="left:112px">
  <div class="service-photo" role="img" aria-label="Smartphone showing a colourful sign-in screen" style="background:linear-gradient(120deg,#2a2a2e 0%,#3a3a40 30%,#e8456a 45%,#f0a030 60%,#3f9fd9 78%,#2a2a2e 100%)"></div>
  <h3>Personal cards in one minute</h3>
</div>
<div class="service" style="left:293px">
  <div class="service-photo" role="img" aria-label="Hand holding a tablet showing a contacts app" style="background:linear-gradient(160deg,#d8d2c6 0%,#bfc8b0 40%,#e9e6df 70%,#b79a86 100%)"></div>
  <h3>Send to your whole address book</h3>
</div>
<div class="service" style="left:474px">
  <div class="service-photo" role="img" aria-label="Woman using her phone on a city street" style="background:linear-gradient(90deg,#5b4a44 0%,#8a6a5c 40%,#3c3030 65%,#a0a6ae 100%)"></div>
  <h3>Smart pricing for businesses</h3>
</div>

<section class="band"></section>
<svg class="laptop" width="276" height="162" viewBox="0 0 276 162">
  <rect x="26" y="0" width="224" height="152" rx="6" fill="#1b1b1b"/>
  <rect x="34" y="8" width="208" height="136" fill="#7c8a96"/>
  <rect x="0" y="152" width="276" height="8" rx="3" fill="#cfcfcf"/>
  <rect x="0" y="158" width="276" height="3" rx="1.5" fill="#9a9a9a"/>
</svg>
<div class="abs" role="img" aria-label="Video still of a finger tapping a smartphone screen" style="left:147px;top:860px;width:208px;height:136px;background:linear-gradient(120deg,#4b5b6a 0%,#c9a58c 35%,#e5ddd4 55%,#8aa0b4 100%)"></div>
<svg class="abs" style="left:234px;top:909px" width="34" height="34" viewBox="0 0 34 34"><circle cx="17" cy="17" r="16" fill="rgba(60,60,60,.55)"/><polygon points="13,10 25,17 13,24" fill="#fff"/></svg>
<h2 class="band-title">What is this</h2>
<p class="band-text">Snap for Post is an online postcard app. Pick a photo from your phone or computer, write your message and add the address. We print your card on thick premium paper and post it for you the same day, to any country. No stamps, no queue at the post office. Watch the short video to see how easy it is, then create a free account and send your first card.</p>
<a class="band-button" href="#">Create account or log in</a>

<h2 class="clients-title">Our Clients</h2>
<div class="clients-nav">‹›</div>
<div class="client" style="left:112px">Stayvia</div>
<div class="client" style="left:218px">Crowdly</div>
<div class="client" style="left:324px">Facetra</div>
<div class="client" style="left:430px">Milo Varden</div>
<div class="client" style="left:535px">Polar Peak</div>

<footer class="site-footer">
  <div class="footer-links">HOME<span>|</span>ABOUT US<span>|</span>SERVICES<span>|</span>FEATURES<span>|</span>CONTACT US</div>
  <div class="copyright">© 2013, SNAP FOR POST. ALL RIGHTS RESERVED.</div>
  <div class="follow">FOLLOW US :</div>
  <div class="social" style="left:543px"></div>
  <div class="social" style="left:561px"></div>
  <div class="social" style="left:580px"></div>
  <div class="social" style="left:599px"></div>
  <div class="social" style="left:618px"></div>
</footer>
</body>
</html>
```